Simple Easy - Taekwondo brochure

I have the content and an idea of the layout I want. I need it to look nice and sharp.

It's a sided 8.5x11 colored brochure

please feel free to move things around and use the images provided

my website is www.brightpathdojo.example if you need an understanding of what the business is about.

all text content is on the website. please be creative!

Target Market(s)

Mothers...must by family friendly because it's for mothers to bring their kids.

Industry/Entity Type

Martial Art

Font styles to use
Other font styles liked:
• Lato

```html
<!DOCTYPE html>
<html lang="en">
<head>
<meta charset="utf-8">
<title>Bright Path Dojo – Trifold Brochure</title>
<link rel="stylesheet" href="https://fonts.googleapis.com/css2?family=Lato:wght@400;700;900&family=Oswald:wght@500;700&family=Libre+Baskerville&family=Quicksand:wght@400&family=Roboto:wght@700&display=swap">
<style>
:root{
  --backdrop:#d3a1a3;
  --paper:#efefef;
  --red:#c91f26;
  --red-deep:#a8161c;
  --blue:#1f67b1;
  --navy:#1b4f8c;
  --charcoal:#3b3c3e;
  --ink:#4a4a4a;
  --white:#ffffff;
}
*{box-sizing:border-box;margin:0;padding:0}
html,body{width:1200px;height:1200px;overflow:hidden}
body{background:var(--backdrop);position:relative;font-family:'Lato',sans-serif;color:var(--ink)}
.sheet{position:absolute;left:245px;width:710px;height:548px;box-shadow:0 2px 8px rgba(0,0,0,.25);overflow:hidden;background:var(--paper)}
.sheet--outside{top:34px}
.sheet--inside{top:618px}
.sheet__art{position:absolute;inset:0}
.abs{position:absolute}
.tag{position:absolute;background:var(--red);color:var(--white);font:700 10px 'Lato',sans-serif;padding:3px 10px 3px 18px;clip-path:polygon(0 0,100% 8%,94% 100%,0 92%)}
.body-copy{position:absolute;font-size:7.4px;line-height:9.6px;text-align:justify;color:#555}
.body-copy p+p{margin-top:9.6px}
.url{position:absolute;bottom:5px;width:237px;text-align:center;color:var(--white);font:700 7.5px 'Lato',sans-serif;letter-spacing:2.5px;white-space:nowrap}
.callbar{position:absolute;bottom:5px;left:233px;width:238px;text-align:center;color:var(--white);font:400 8px 'Lato',sans-serif;display:flex;justify-content:center;align-items:center;gap:3px}
.callbar svg{width:12px;height:12px}
.offer__title{left:233px;width:238px;top:186px;text-align:center;font:400 16px 'Libre Baskerville',serif;color:#444}
.offer__box{left:289px;top:212px;width:126px;height:80px;border:2px solid #8fb3dd;border-radius:5px;background:#fafafa;text-align:center;box-shadow:0 1px 3px rgba(0,0,0,.2);white-space:nowrap}
.offer__pct{font:700 29px/36px 'Oswald',sans-serif;color:var(--red);margin-top:4px}
.offer__line{font:400 9px/12px 'Lato',sans-serif;color:var(--blue);letter-spacing:.3px;margin-top:4px}
.address{left:233px;width:238px;top:505px;text-align:center;color:var(--white);font-size:7.6px;display:flex;justify-content:center;gap:3px;align-items:center;white-space:nowrap}
.brand-name{left:592px;top:122px;width:115px;text-align:center;color:var(--white);font:900 10px/14px 'Lato',sans-serif;letter-spacing:.5px}
.headline{left:471px;width:239px;text-align:center;line-height:1;white-space:nowrap}
.headline--focus{top:397px;font:700 29px 'Roboto',sans-serif;color:var(--white)}
.headline--child{top:432px;font:700 32px 'Oswald',sans-serif;color:var(--red);letter-spacing:.5px}
.headline--potential{top:472px;font:700 29px 'Roboto',sans-serif;color:var(--white)}
.intro{left:10px;width:213px;top:166px;text-align:center;font-size:10px;line-height:12px;color:#555}
.benefit{position:absolute;width:110px;text-align:center;font-size:10px;color:#555}
.benefit svg{display:block;margin:0 auto 3px;width:16px;height:14px}
.discipline{left:233px;width:238px;top:16px;text-align:center;font:700 35px/36px 'Oswald',sans-serif;color:var(--red);letter-spacing:.5px}
.motto{left:233px;width:238px;top:58px;text-align:center;font:400 10px/12px 'Quicksand',sans-serif;color:#555}
.tenets-bar{left:233px;width:238px;top:75px;height:17px;background:var(--navy);color:var(--white);text-align:center;font:700 9.5px/17px 'Lato',sans-serif}
.tenets-row{left:240px;width:224px;top:106px;display:flex;justify-content:space-between;font:700 4.6px 'Oswald',sans-serif;color:#555}
.tenets-row span::before{content:"";display:inline-block;width:4px;height:4px;border-radius:50%;background:var(--red);margin-right:2px;vertical-align:middle}
.tenet-copy{position:absolute;width:203px;font-size:7.3px;line-height:9.6px;text-align:justify;text-align-last:center;color:#555}
.character{left:233px;width:238px;top:176px;text-align:center;font-size:7.3px;color:#555}
.num{position:absolute;width:32px;height:32px;border-radius:50%;background:var(--white);border:2px solid #cfd6de;box-shadow:0 1px 2px rgba(0,0,0,.15);text-align:center;font:400 20px/28px 'Lato',sans-serif;color:var(--blue)}
.tenet-title{position:absolute;width:238px;text-align:center;font:400 10.5px 'Lato',sans-serif;color:var(--red);letter-spacing:.2px}
.art-label{position:absolute;top:508px;font:700 8px 'Lato',sans-serif;letter-spacing:3px}
</style>
</head>
<body>

<section class="sheet sheet--outside">
  <svg class="sheet__art" width="710" height="548" viewBox="0 0 710 548">
    <defs>
      <linearGradient id="paperA" x1="0" y1="0" x2="1" y2="1"><stop offset="0" stop-color="#f3f3f3"/><stop offset="1" stop-color="#e3e3e3"/></linearGradient>
      <linearGradient id="portrait" x1="0" y1="0" x2="0" y2="1"><stop offset="0" stop-color="#c9a58a"/><stop offset=".3" stop-color="#f2f2f2"/><stop offset="1" stop-color="#d6d6d6"/></linearGradient>
      <linearGradient id="belt" x1="0" y1="0" x2="1" y2="1"><stop offset="0" stop-color="#e9e9e9"/><stop offset=".6" stop-color="#bdbdbd"/><stop offset="1" stop-color="#2a2a2a"/></linearGradient>
      <pattern id="mesh" width="6" height="6" patternUnits="userSpaceOnUse"><rect width="6" height="6" fill="#2e2f31"/><circle cx="3" cy="3" r="1.5" fill="#1b1c1d"/></pattern>
    </defs>
    <rect width="710" height="548" fill="url(#paperA)"/>
    <rect x="233" width="238" height="548" fill="#f0f0f0"/>
    <rect x="471" width="239" height="548" fill="var(--charcoal)"/>
    <polygon points="471,0 710,0 710,50 471,160" fill="var(--red)"/>
    <line x1="471" y1="166" x2="710" y2="56" stroke="#fff" stroke-width="3"/>
    <line x1="471" y1="171" x2="710" y2="61" stroke="var(--blue)" stroke-width="4"/>
    <g role="img" aria-label="Photo of the head instructor in a white dobok with arms crossed, red paint splash behind">
      <rect x="473" y="52" width="112" height="322" fill="url(#portrait)"/>
      <rect x="473" y="170" width="192" height="204" fill="url(#portrait)"/>
    </g>
    <rect x="0" y="382" width="210" height="144" fill="url(#belt)" role="img" aria-label="Photo of hands tying a black belt over a white uniform"/>
    <polygon points="150,503 710,310 710,548 150,548" fill="url(#mesh)"/>
    <line x1="150" y1="496" x2="710" y2="303" stroke="var(--red)" stroke-width="5"/>
    <line x1="150" y1="491" x2="710" y2="298" stroke="#fff" stroke-width="3"/>
    <line x1="150" y1="487" x2="710" y2="294" stroke="var(--blue)" stroke-width="4"/>
    <polygon points="351,326 431,370 431,452 351,496 271,452 271,370" fill="var(--blue)"/>
    <polygon points="351,336 422,375 422,447 351,486 280,447 280,375" fill="#fff"/>
    <polygon points="351,342 416,378 416,444 351,480 286,444 286,378" fill="#e4e6e2" role="img" aria-label="Street map showing the dojo location"/>
    <path d="M344,397 a5,5 0 1 1 10,0 c0,4 -5,9 -5,9 c0,0 -5,-5 -5,-9z" fill="var(--red)"/>
    <circle cx="649" cy="66" r="44" fill="#fff" stroke="var(--blue)" stroke-width="3"/>
    <polygon points="28,526 682,526 690,548 20,548" fill="var(--red)"/>
    <polygon points="0,532 28,526 20,548 0,548" fill="var(--blue)"/>
    <polygon points="682,526 710,532 710,548 690,548" fill="var(--blue)"/>
    <line x1="233" y1="0" x2="233" y2="548" stroke="rgba(0,0,0,.06)"/>
    <line x1="471" y1="0" x2="471" y2="548" stroke="rgba(0,0,0,.1)"/>
  </svg>

  <div class="tag" style="left:0;top:16px">Master Dan</div>
  <div class="body-copy" style="left:18px;top:42px;width:196px">
    <p>Daniel Park, (Master Dan), is the owner and head instructor at Bright Path Dojo. Master Dan is a certified 3rd degree Black Belt of the National Dan Council, the overseeing authority of all Black Belts in the world, working with the Global Taekwondo Union (GTU); it also oversees taekwondo in the Olympics. In 1992, at the age of 8, Master Dan began training under Grand Master Moretti who achieved the level of 8th Dan in taekwondo under the International Taekwondo Alliance (ITA). The ITA is another highly respected global authority for taekwondo. When Master Dan entered Middle School and then High School, his years of taekwondo training became invaluable as he participated in wrestling, track, and hockey.</p>
    <p>Master Dan continued his taekwondo training post-high school, and in 2007, began training under Grand Master Kang who has achieved the level of 6th Dan in Taekwondo, certified by the Council; Grand Master Kang was also a distinguished member of the South Korean National Taekwondo Team that competed around the world.</p>
    <p>While attending Riverside University, Master Dan joined the university Taekwondo Team. Upon graduating in 2008, he was invited by the University to become the team's Assistant Coach. Because of his exceptional skill and his ability to positively influence and motivate the team, the University selected him to lead as the coach of the team. Master Dan served as the Head Coach of the Riverside University Taekwondo Team from 2010-2013.</p>
    <p>In 2013, Master Dan began training under Grand Master Yoon, a 9th Dan in Taekwondo, certified by the Council. Master Dan currently trains under Grand Master Yoon.</p>
  </div>
  <div class="url" style="left:0">www.brightpathdojo.example</div>

  <div class="tag" style="left:233px;top:16px">Rachel T.</div>
  <div class="body-copy" style="left:251px;top:42px;width:202px">
    <p>I started taking classes with Master Dan a little over 3 years ago. As the newest member of the class, I was shy and unsure of myself. However, I quickly overcame those feelings because Master Dan is a natural teacher. Paired with his passion for the sport, his gift for teaching makes him one of the best coaches I have encountered. I have seen him work with both children and adults and his manner is unfailingly supportive and encouraging. As a teacher myself, I see how he tailors his teaching style to each student and I hope to follow his example in my classroom. I am thankful that my first experience with taekwondo has been through Master Dan's class.</p>
  </div>
  <div class="abs offer__title">Special Offer</div>
  <div class="abs offer__box">
    <div class="offer__pct">50% OFF</div>
    <div class="offer__line">TRIAL LESSONS AND<br>GET A FREE T-SHIRT!</div>
  </div>
  <div class="abs address">
    <svg width="8" height="10" viewBox="0 0 8 10"><path d="M4,0 a4,4 0 0 1 4,4 c0,3 -4,6 -4,6 c0,0 -4,-3 -4,-6 a4,4 0 0 1 4,-4z M4,2.3 a1.7,1.7 0 1 0 0.01,0z" fill="#fff" fill-rule="evenodd"/></svg>
    2750 Maple Ridge Road, Fairview, PA 19400
  </div>
  <div class="callbar">Call us today!
    <svg viewBox="0 0 12 12"><circle cx="6" cy="6" r="5.4" fill="none" stroke="#fff"/><path d="M4,3.2 l1,1.3 -.6,.7 c.4,.9 1,1.5 1.9,1.9 l.7-.6 1.3,1 -.7,1 c-2.2,-.3 -4,-2.1 -4.3,-4.3z" fill="#fff"/></svg>
    555-014-2938</div>

  <div class="abs brand-name">BRIGHT PATH<br>DOJO</div>
  <div class="abs headline headline--focus">Focus</div>
  <div class="abs headline headline--child">YOUR CHILD'S</div>
  <div class="abs headline headline--potential">Potential</div>
  <div class="url" style="left:473px">www.brightpathdojo.example</div>
</section>

<section class="sheet sheet--inside">
  <svg class="sheet__art" width="710" height="548" viewBox="0 0 710 548">
    <defs>
      <linearGradient id="paperB" x1="0" y1="0" x2="1" y2="1"><stop offset="0" stop-color="#f2f2f2"/><stop offset="1" stop-color="#e4e4e4"/></linearGradient>
      <linearGradient id="tigerTones" x1="0" y1="0" x2="1" y2="1"><stop offset="0" stop-color="#e9a25c"/><stop offset=".5" stop-color="#f6f1ea"/><stop offset="1" stop-color="#d98a3e"/></linearGradient>
      <linearGradient id="bamboo" x1="0" y1="0" x2="0" y2="1"><stop offset="0" stop-color="#a9c96a"/><stop offset="1" stop-color="#6a8f3a"/></linearGradient>
      <linearGradient id="fadeHands" x1="0" y1="0" x2="0" y2="1"><stop offset="0" stop-color="#e8e8e8" stop-opacity="0"/><stop offset="1" stop-color="#c9c9c9"/></linearGradient>
      <pattern id="mesh2" width="6" height="6" patternUnits="userSpaceOnUse"><rect width="6" height="6" fill="#2e2f31"/><circle cx="3" cy="3" r="1.5" fill="#1b1c1d"/></pattern>
    </defs>
    <rect width="710" height="548" fill="url(#paperB)"/>
    <rect x="233" width="238" height="548" fill="#f1f1f1"/>
    <polygon points="471,0 710,0 710,95" fill="var(--red)"/>
    <line x1="430" y1="0" x2="710" y2="112" stroke="var(--blue)" stroke-width="4"/>
    <line x1="438" y1="0" x2="710" y2="107" stroke="#fff" stroke-width="3"/>
    <polygon points="0,408 233,500 233,548 0,548" fill="url(#mesh2)"/>
    <line x1="0" y1="392" x2="233" y2="484" stroke="var(--blue)" stroke-width="4"/>
    <line x1="0" y1="397" x2="233" y2="489" stroke="#fff" stroke-width="3"/>
    <line x1="0" y1="402" x2="233" y2="494" stroke="var(--red)" stroke-width="5"/>
    <rect x="38" y="14" width="165" height="132" rx="8" fill="url(#tigerTones)" opacity=".8" role="img" aria-label="Cartoon tiger cub in a dobok holding a magnifying glass beside a small tiger"/>
    <rect x="40" y="340" width="178" height="160" rx="8" fill="url(#tigerTones)" opacity=".85" role="img" aria-label="Cartoon tiger in a dobok holding a bamboo staff in a fighting stance"/>
    <rect x="254" y="418" width="196" height="88" rx="6" fill="url(#bamboo)" opacity=".8" role="img" aria-label="Three cartoon bamboo shoot characters showing growth stages"/>
    <rect x="475" y="430" width="232" height="90" fill="url(#fadeHands)" role="img" aria-label="Faded photo of a student's hands tying a belt"/>
    <rect x="233" y="526" width="238" height="22" fill="var(--red-deep)"/>
    <polygon points="28,526 682,526 690,548 20,548" fill="var(--red)"/>
    <polygon points="0,532 28,526 20,548 0,548" fill="var(--blue)"/>
    <polygon points="682,526 710,532 710,548 690,548" fill="var(--blue)"/>
    <line x1="233" y1="0" x2="233" y2="548" stroke="rgba(0,0,0,.08)"/>
    <line x1="471" y1="0" x2="471" y2="548" stroke="rgba(0,0,0,.08)"/>
  </svg>

  <div class="abs intro">Bright Path Dojo is the perfect tool to unlocking your child's potential.</div>
  <div class="benefit" style="left:4px;top:206px"><svg viewBox="0 0 16 14"><g fill="var(--blue)"><circle cx="3" cy="3" r="2"/><circle cx="8" cy="3" r="2"/><circle cx="13" cy="3" r="2"/><rect x="1" y="6" width="4" height="7"/><rect x="6" y="6" width="4" height="7" fill="var(--red)"/><rect x="11" y="6" width="4" height="7"/></g></svg>Discipline</div>
  <div class="benefit" style="left:117px;top:206px"><svg viewBox="0 0 16 14"><circle cx="6" cy="3" r="2" fill="var(--red)"/><path d="M6,6 l4,0 0,7 -2,0 0,-5 -2,0z" fill="var(--blue)"/></svg>Self-Respect</div>
  <div class="benefit" style="left:4px;top:250px"><svg viewBox="0 0 16 14"><circle cx="9" cy="2.5" r="2" fill="var(--red)"/><path d="M2,4 l6,3 0,3 3,4 -2,0 -3,-3 -4,-6z" fill="var(--blue)"/></svg>Self-Defense</div>
  <div class="benefit" style="left:117px;top:250px"><svg viewBox="0 0 16 14"><g fill="var(--blue)"><circle cx="4" cy="4" r="2"/><circle cx="12" cy="4" r="2"/><rect x="2" y="7" width="4" height="6"/><rect x="10" y="7" width="4" height="6"/></g><circle cx="8" cy="3" r="2" fill="var(--red)"/><rect x="6" y="6" width="4" height="7" fill="var(--red)"/></svg>Leadership</div>
  <div class="benefit" style="left:4px;top:296px"><svg viewBox="0 0 16 14"><g fill="var(--blue)"><circle cx="5" cy="5" r="2"/><rect x="3" y="8" width="4" height="5"/><circle cx="11" cy="6" r="2"/><rect x="9" y="9" width="4" height="4"/></g><circle cx="12" cy="2" r="1.5" fill="var(--red)"/></svg>Focus</div>
  <div class="benefit" style="left:117px;top:296px"><svg viewBox="0 0 16 14"><path d="M8,1 l5,2 0,4 c0,3 -2.5,5 -5,6 c-2.5,-1 -5,-3 -5,-6 l0,-4z" fill="none" stroke="var(--blue)" stroke-width="1.4"/><circle cx="8" cy="7" r="1.8" fill="var(--red)"/></svg>Anti-Bullying</div>
  <div class="art-label" style="left:0;width:233px;text-align:center;color:#5a9be0">PROTECT</div>
  <div class="url" style="left:0">www.brightpathdojo.example</div>

  <div class="abs discipline">DISCIPLINE</div>
  <div class="abs motto">Love discipline. Love knowledge</div>
  <div class="abs tenets-bar">The Five Tenets of Taekwondo</div>
  <div class="abs tenets-row"><span>COURTESY</span><span>INTEGRITY</span><span>PERSEVERANCE</span><span>SELF-CONTROL</span><span>INDOMITABLE SPIRIT</span></div>
  <div class="tenet-copy" style="left:250px;top:124px">There are five universally accepted tenets of taekwondo accepted by both the Global Taekwondo Union (GTU) and the International Taekwondo Alliance (ITA). Bright Path Dojo bases our dojang rules and etiquette on the "Five Tenets of Taekwondo."</div>
  <div class="abs character">(The Building of Character)</div>
  <div class="num" style="left:336px;top:200px">1</div>
  <div class="tenet-title" style="left:233px;top:236px">COURTESY</div>
  <div class="tenet-copy" style="left:250px;top:256px">Students will show courtesy to all others in the dojang, as well as people they meet outside of their formal training. Younger students will address adults as "Sir" or "Ma'am." Students will bow to the American and S. Korean flags upon entering and exiting the dojang.</div>
  <div class="num" style="left:336px;top:321px">2</div>
  <div class="tenet-title" style="left:233px;top:359px">INTEGRITY</div>
  <div class="tenet-copy" style="left:250px;top:380px">Students are expected to be honest and be willing to exhibit strong moral principles that will help them distinguish between right and wrong.</div>
  <div class="art-label" style="left:258px;color:#8fc0ea">GROW</div>
  <div class="art-label" style="left:338px;color:#8fc0ea">ROOT</div>
  <div class="art-label" style="left:408px;color:var(--red)">THRIVE</div>
  <div class="callbar">Call us today!
    <svg viewBox="0 0 12 12"><circle cx="6" cy="6" r="5.4" fill="none" stroke="#fff"/><path d="M4,3.2 l1,1.3 -.6,.7 c.4,.9 1,1.5 1.9,1.9 l.7-.6 1.3,1 -.7,1 c-2.2,-.3 -4,-2.1 -4.3,-4.3z" fill="#fff"/></svg>
    555-014-2938</div>

  <div class="num" style="left:575px;top:67px">3</div>
  <div class="tenet-title" style="left:472px;top:104px">PERSEVERANCE</div>
  <div class="tenet-copy" style="left:490px;top:124px">Students must remember that they will never grow stronger by engaging their doubts. Therefore, students should be willing to confront their fears, battle back against their struggles, and never look for short-cuts when achieving their goals.</div>
  <div class="num" style="left:575px;top:199px">4</div>
  <div class="tenet-title" style="left:472px;top:236px">SELF-CONTROL</div>
  <div class="tenet-copy" style="left:490px;top:256px">Students are expected to keep their emotions (thoughts and actions) in-check at all times, both inside and outside the dojang. Punctuality is essential because all classes start promptly at the designated times. Students are expected to keep the dojang clean and tidy.</div>
  <div class="num" style="left:575px;top:322px">5</div>
  <div class="tenet-title" style="left:472px;top:359px">INDOMITABLE SPIRIT</div>
  <div class="tenet-copy" style="left:490px;top:380px">Indomitable Spirit – Students will consistently exhibit a full 100% effort in all they do inside and outside the dojang. Students must show courage when standing up for their beliefs and convictions inside and outside the dojang.</div>
  <div class="url" style="left:473px">www.brightpathdojo.example</div>
</section>

</body>
</html>
```